Flyer-Design für Fusspflege für den Mann
schade dass die Daten nicht auch im psd-format geliefert werden konnten
Zielgruppe
Fusspflege und Maniküre für den Mann - neu und zusammen in einem Haarentfernungsinstitut für Männer in Zürich
Aufgabenstellung
Sie haben freie Wahl - Farben an das Logo angepasst.
Für tolle Bilder bin ich offen.
Sollte auch stehen: nur auf Voranmeldung - am besten per SMS
Zudem das persönliche Foto dazu

```html
<!DOCTYPE html>
<html lang="de">
<head>
<meta charset="utf-8">
<title>PediNova Flyer – Hand- und Fusspflege für den Mann</title>
<link href="https://fonts.googleapis.com/css2?family=Open+Sans:wght@400;600;700;800&display=swap" rel="stylesheet">
<style>
:root{
  --brown:#634529;
  --brown-dark:#4e361f;
  --gold:#c9a22f;
  --gold-light:#f3dd7a;
  --cream:#f7f0dc;
  --band-text:#d8c6a4;
  --red:#b3232b;
  --ink:#3a2a1b;
  --stage:#e4e4e4;
  --white:#ffffff;
}
*{box-sizing:border-box;margin:0;padding:0}
html,body{width:1200px;height:1200px;overflow:hidden}
body{background:var(--stage);font-family:"Open Sans",Arial,sans-serif;color:var(--ink);position:relative}
.flyer{position:absolute;top:60px;width:540px;height:1080px;overflow:hidden;box-shadow:0 4px 14px rgba(0,0,0,.18)}
.flyer--front{left:40px;background:var(--white)}
.flyer--back{left:620px;background:var(--cream)}

/* front */
.hero-photo{position:absolute;left:0;top:0;width:540px;height:540px;
  background:radial-gradient(circle at 60% 70%,#d9b58c 0%,#b89271 40%,#8e6d52 100%)}
.badge{position:absolute;left:28px;top:40px;width:150px;height:150px;border-radius:50%;
  background:var(--red);border:4px solid var(--white);color:var(--white);
  display:flex;align-items:center;justify-content:center;text-align:center;
  font-weight:700;font-size:17px;line-height:1.2;padding:0 14px 8px}
.headline{position:absolute;left:20px;width:480px;top:255px;text-align:center;
  font-weight:800;font-size:40px;line-height:1.12;color:var(--gold-light);
  text-shadow:0 0 3px var(--brown-dark),2px 2px 4px rgba(60,40,20,.7)}
.brown-panel{position:absolute;left:0;top:510px;width:540px;height:410px;background:var(--brown)}
.portrait{position:absolute;left:135px;top:430px;width:250px;height:250px;border-radius:50%;
  border:5px solid var(--gold);background:linear-gradient(160deg,#a37c5c,#5a3d29)}
.booking{position:absolute;left:0;width:540px;top:700px;text-align:center;color:var(--white)}
.booking__note{font-weight:700;font-size:17px;line-height:1.35}
.booking__phone{font-weight:700;font-size:32px;line-height:1.2;margin-top:6px;letter-spacing:.5px}
.footer-curve{position:absolute;left:0;top:830px}
.brand{position:absolute;left:50px;top:955px;display:flex;align-items:center;gap:12px}
.brand__dot{width:26px;height:26px;border-radius:50%;background:var(--gold)}
.brand__name{font-weight:700;font-size:34px;color:var(--brown)}
.contact{position:absolute;left:320px;top:932px;font-size:15px;line-height:1.3;color:var(--ink);font-style:normal}
.contact strong{color:var(--gold);font-weight:700}
.contact__web{display:block;margin-top:14px;color:var(--gold);font-weight:700;font-size:17px}

/* back */
.band{position:absolute;left:0;width:540px;background:var(--brown)}
.band__title{position:absolute;font-weight:800;color:var(--band-text);letter-spacing:1px}
.thumb{position:absolute;width:130px;height:130px;border-radius:50%;border:3px solid var(--gold);
  background:linear-gradient(150deg,#efe6d6,#b9a58c)}
.service{position:absolute;left:50px;width:450px}
.service__head{display:flex;align-items:baseline;font-weight:700;color:var(--gold);font-size:19px}
.service__name{flex:1}
.service__time{width:110px}
.service__price{width:55px;text-align:right}
.service__sub{font-weight:700;font-size:13px;color:var(--ink);margin-top:2px}
.service__desc{font-size:13px;line-height:1.35;margin-top:3px}
</style>
</head>
<body>

<section class="flyer flyer--front">
  <div class="hero-photo" role="img" aria-label="Foto: Hände massieren einen Fuss über einer Holzschale mit Blüten"></div>
  <div class="badge">Hand- und Fusspflege für den Mann</div>
  <h1 class="headline">Nur das Beste<br>für Deine Hände<br>und Füsse</h1>
  <div class="brown-panel"></div>
  <div class="portrait" role="img" aria-label="Porträtfoto des Fusspflegers"></div>
  <div class="booking">
    <p class="booking__note">Nur auf Voranmeldung!<br>Am besten per WhatsApp oder per SMS</p>
    <p class="booking__phone">079 555 31 27</p>
  </div>
  <svg class="footer-curve" width="540" height="250" viewBox="0 0 540 250" aria-hidden="true">
    <path d="M0,75 Q270,-15 540,10 L540,250 L0,250 Z" fill="var(--gold)"/>
    <path d="M0,85 Q270,0 540,22 L540,250 L0,250 Z" fill="var(--white)"/>
  </svg>
  <div class="brand">
    <span class="brand__dot"></span>
    <span class="brand__name">PediNova</span>
  </div>
  <address class="contact">
    <strong>PediNova by Glattwerk</strong><br>
    <strong>Luca Brandt</strong><br>
    Feldweg 14<br>
    CH-8005 Zürich<br>
    luca@glattwerk.ch
    <span class="contact__web">www.glattwerk.ch</span>
  </address>
</section>

<section class="flyer flyer--back">
  <div class="band" style="top:100px;height:95px">
    <span class="band__title" style="right:30px;top:20px;font-size:44px">HÄNDE</span>
  </div>
  <div class="thumb" style="left:35px;top:70px" role="img" aria-label="Foto: Nagelfeile an einer Hand"></div>
  <article class="service" style="top:230px">
    <div class="service__head"><span class="service__name">Die klassische Maniküre</span><span class="service__time">40 Min</span><span class="service__price">48.-</span></div>
    <p class="service__desc">Hände reinigen &amp; desinfizieren · Nägel formen · Nagelhaut korrigieren · Hand- &amp; Nagelbalsam · Kleine Handmassage</p>
  </article>

  <div class="band" style="top:360px;height:85px">
    <span class="band__title" style="left:40px;top:18px;font-size:44px">FÜSSE</span>
  </div>
  <div class="thumb" style="right:30px;top:335px" role="img" aria-label="Foto: Fussbehandlung mit Handschuhen"></div>
  <article class="service" style="top:490px">
    <div class="service__head"><span class="service__name">Der Klassiker</span><span class="service__time">60 Min</span><span class="service__price">85.-</span></div>
    <p class="service__desc">Füsse reinigen &amp; desinfizieren · Nägel kürzen, feilen und fräsen · Nagelhäutchen und Nagelfalz reinigen · Hornhaut entfernen · Kleine Fussmassage</p>
  </article>
  <article class="service" style="top:590px">
    <div class="service__head"><span class="service__name">Das Hammerding</span><span class="service__time">80 Min</span><span class="service__price">115.-</span></div>
    <p class="service__sub">Das Rundum-Sorglos-Programm für Füße</p>
    <p class="service__desc">Füsse reinigen &amp; desinfizieren · Nägel kürzen, feilen und fräsen · Nagelhäutchen und Nagelfalz reinigen · Hornhaut entfernen · Fusspeeling · Fussbad · Fussmassage</p>
  </article>

  <div class="band" style="top:755px;height:85px">
    <span class="band__title" style="right:30px;top:16px;font-size:18px;text-align:right;line-height:1.35">GÖNN DIR EIN KLEINES<br>WOHLFÜHLPLUS</span>
  </div>
  <div class="thumb" style="left:35px;top:730px" role="img" aria-label="Foto: Füsse mit Blüten im Fussbad"></div>
  <article class="service" style="top:875px">
    <div class="service__head"><span class="service__name">Das Paraffinbad</span><span class="service__time">20 Min</span><span class="service__price">28.-</span></div>
    <p class="service__desc">Endlich wieder glatte Haut an den Händen oder Füssen. Entspannend und hautpflegend mit Kollagen und AloeVera; die Haut wird mit Feuchtigkeit und Pflegstoffe versorgt. Durch die Wärme können Schmerzen gelindert werden.</p>
  </article>
  <article class="service" style="top:995px">
    <div class="service__head"><span class="service__name">Die Happy Fussmassage</span><span class="service__time">25 Min</span><span class="service__price">48.-</span></div>
    <p class="service__desc">Verwöhnung und leichtere Füsse<br>Eine wohltuende und entspannende Fussmassage</p>
  </article>
</section>

</body>
</html>
```